Quorvix Letter head

Quorvix is a young and energetic software development consultancy. We spend our time working with clients to turn what ever is in their heads in to software.
We are trying to create an image of a high class software boutique who build class leading bespoke solutions.
We need a sharp letter head that looks great on high quality media.
We like bold colours and distinctive design. So show us what you can do.
Industry/Entity Type
Software
Requirements
Must have
- Our company is based in the UK and are requried to have on the paper somewhere the following information:
* Registered company name: Quorvix Ltd
* Registered company number
* VAT registration number
In addition we also want the following:
* An email address
* Telephone number
* Website address
An example of what some pages have in their footer is something like the following:
Quorvix Ltd is registered in England and Wales. Reg. no: 5316274
Registered office: 48 Cobblewick Road, Harlow Essex, CM93TP. Tel: 07712365081
You do not have to use this sentance but please make sure your design incorporates accommodates the requirements for UK based companies

```html
<!DOCTYPE html>
<html lang="en">
<head>
<meta charset="utf-8">
<title>Quorvix Letterhead</title>
<link rel="stylesheet" href="https://fonts.googleapis.com/css2?family=Montserrat:wght@400;500&display=swap">
<style>
  :root {
    --brand-red: #c0212f;
    --watermark-pink: #f8e1e3;
    --page-edge: #e6e6e6;
    --paper: #ffffff;
    --canvas: #ffffff;
    --legal-grey: #5a5a5a;
  }
  html, body {
    margin: 0;
    padding: 0;
    width: 1200px;
    height: 973px;
    overflow: hidden;
    background: var(--canvas);
  }
  .sheet-set {
    display: block;
    width: 1200px;
    height: 973px;
  }
  .page { fill: var(--paper); stroke: var(--page-edge); stroke-width: 2; }
  .rule { stroke: var(--brand-red); stroke-width: 3; fill: none; }
  .rule--heavy { stroke-width: 5; }
  .wordmark {
    font-family: "Montserrat", sans-serif;
    font-weight: 500;
    fill: var(--brand-red);
  }
  .watermark {
    font-family: "Montserrat", sans-serif;
    font-weight: 500;
    fill: var(--watermark-pink);
  }
  .legal {
    font-family: "Montserrat", sans-serif;
    font-weight: 400;
    font-size: 7.6px;
    fill: var(--legal-grey);
  }
  .legal-name { fill: var(--brand-red); font-weight: 500; }
</style>
</head>
<body>
<svg class="sheet-set" viewBox="0 0 1240 1005" xmlns="http://www.w3.org/2000/svg" role="group" aria-label="Quorvix letterhead, two page variants">

  <!-- Variant A: vertical side band -->
  <g class="letterhead letterhead--side">
    <rect class="page" x="26" y="100" width="567" height="801"/>
    <g class="side-rules">
      <line class="rule" x1="49" y1="120" x2="49" y2="881"/>
      <line class="rule" x1="61" y1="156" x2="61" y2="384"/>
      <line class="rule" x1="74" y1="207" x2="74" y2="384"/>
      <line class="rule" x1="86" y1="255" x2="86" y2="384"/>
      <line class="rule" x1="99" y1="299" x2="99" y2="384"/>
      <line class="rule" x1="112" y1="341" x2="112" y2="384"/>
      <line class="rule" x1="124" y1="385" x2="124" y2="881"/>
      <line class="rule" x1="61" y1="746" x2="61" y2="881"/>
      <line class="rule" x1="74" y1="746" x2="74" y2="881"/>
      <line class="rule" x1="86" y1="746" x2="86" y2="881"/>
      <line class="rule" x1="99" y1="746" x2="99" y2="881"/>
      <line class="rule" x1="112" y1="746" x2="112" y2="881"/>
    </g>
    <text class="wordmark" transform="translate(114 740) rotate(-90)" font-size="74" textLength="350" lengthAdjust="spacingAndGlyphs">QUORVIX</text>
    <text class="legal" text-anchor="end">
      <tspan class="legal-name" x="578" y="860">Quorvix Ltd · Registered in England and Wales · Reg. no: 5316274 · VAT no: GB 418 2093 57</tspan>
      <tspan x="578" y="872">Registered office: 48 Cobblewick Road, Harlow Essex, CM93TP</tspan>
      <tspan x="578" y="884">Tel: 07712365081 · hello@quorvix.co.uk · www.quorvix.co.uk</tspan>
    </text>
  </g>

  <!-- Variant B: top header band -->
  <g class="letterhead letterhead--top">
    <rect class="page" x="641" y="100" width="567" height="801"/>
    <text class="watermark" transform="translate(790 690) rotate(-45)" font-size="116" textLength="500" lengthAdjust="spacingAndGlyphs">QUORVIX</text>
    <g class="header-rules">
      <line class="rule" x1="651" y1="122" x2="748" y2="122"/>
      <line class="rule" x1="651" y1="131" x2="748" y2="131"/>
      <line class="rule" x1="651" y1="140" x2="748" y2="140"/>
      <line class="rule" x1="651" y1="149" x2="748" y2="149"/>
      <line class="rule" x1="651" y1="158" x2="748" y2="158"/>
      <line class="rule" x1="651" y1="166" x2="1008" y2="166"/>
      <line class="rule" x1="1008" y1="112" x2="1198" y2="112"/>
      <line class="rule" x1="1010" y1="121" x2="1172" y2="121"/>
      <line class="rule" x1="1010" y1="130" x2="1136" y2="130"/>
      <line class="rule" x1="1010" y1="139" x2="1102" y2="139"/>
      <line class="rule" x1="1010" y1="148" x2="1070" y2="148"/>
      <line class="rule" x1="1010" y1="157" x2="1040" y2="157"/>
    </g>
    <text class="wordmark" x="754" y="159" font-size="56" textLength="251" lengthAdjust="spacingAndGlyphs">QUORVIX</text>
    <text class="legal" text-anchor="middle">
      <tspan class="legal-name" x="924.5" y="869">Quorvix Ltd is registered in England and Wales. Reg. no: 5316274 · VAT no: GB 418 2093 57</tspan>
      <tspan x="924.5" y="881">Registered office: 48 Cobblewick Road, Harlow Essex, CM93TP · Tel: 07712365081</tspan>
      <tspan x="924.5" y="891">hello@quorvix.co.uk · www.quorvix.co.uk</tspan>
    </text>
    <line class="rule rule--heavy" x1="651" y1="899" x2="1198" y2="899"/>
  </g>
</svg>
</body>
</html>
```